TIDAL VERGE needs bisness cards pronto

Bisness name is "TIDAL VERGE" new bisness the bisness includes lawn mowing, garden matanace, and any jobs around the house.
I need a card that is colorful and vibrant and the bisness of lawn mowing maybe with some nature with it. It also needs my contact details"Darren Quellby mobile 0413562049 call for free quote and email norma.vance@fernmail.com.au and a catchy tag line

Industry/Entity Type

House

Requirements
Must have
• Bisness name "TIDAL VERGE"
Contact details "0413562049"
Email norma.vance@fernmail.com.au
Call for free quote

```html
<!DOCTYPE html>
<html lang="en">
<head>
<meta charset="utf-8">
<title>Tidal Verge – Business Card</title>
<link rel="stylesheet" href="https://fonts.googleapis.com/css2?family=Cinzel:wght@500&family=Open+Sans:wght@400&display=swap">
<style>
  :root {
    --backdrop-centre: #ffffff;
    --backdrop-edge: #dcdcdc;
    --card-white: #ffffff;
    --meadow-green: #6bbb35;
    --meadow-dark: #2f7a2a;
    --band-green: #b9df84;
    --ink-green: #0d5a2f;
    --rule-yellow: #f7c300;
  }
  html, body {
    margin: 0;
    padding: 0;
    width: 1200px;
    height: 927px;
    overflow: hidden;
  }
  body {
    position: relative;
    background: radial-gradient(ellipse at center, var(--backdrop-centre) 0%, #f3f3f3 45%, var(--backdrop-edge) 100%);
    font-family: "Open Sans", Arial, sans-serif;
  }
  .business-card {
    position: absolute;
    left: 223px;
    top: 254px;
    width: 754px;
    height: 419px;
    background: var(--card-white);
    overflow: hidden;
  }
  .garden-panel {
    position: absolute;
    left: 0;
    top: 0;
    width: 255px;
    height: 100%;
    background: linear-gradient(160deg, var(--meadow-green) 0%, #63b52f 60%, #5aad2b 100%);
  }
  .contact-band {
    position: absolute;
    left: 0;
    top: 0;
  }
  .business-name {
    position: absolute;
    left: 326px;
    top: 52px;
    margin: 0;
    font-family: "Cinzel", "Times New Roman", serif;
    font-weight: 500;
    font-size: 44px;
    line-height: 1;
    letter-spacing: 1px;
    color: var(--ink-green);
    white-space: nowrap;
  }
  .name-rule {
    position: absolute;
    left: 326px;
    top: 115px;
    width: 360px;
    height: 8px;
    background: var(--rule-yellow);
  }
  .service-list {
    position: absolute;
    left: 329px;
    top: 175px;
    margin: 0;
    padding: 0;
    list-style: none;
    font-size: 27px;
    line-height: 33px;
    color: var(--ink-green);
  }
  .quote-line {
    position: absolute;
    left: 313px;
    top: 330px;
    margin: 0;
    font-size: 19px;
    color: var(--ink-green);
    white-space: nowrap;
  }
  .quote-line .phone-number {
    font-size: 28px;
    margin-left: 8px;
    letter-spacing: 0.5px;
  }
  .email-line {
    position: absolute;
    left: 313px;
    top: 376px;
    margin: 0;
    font-size: 19px;
    color: var(--ink-green);
    white-space: nowrap;
  }
</style>
</head>
<body>
  <section class="business-card">
    <div class="garden-panel" role="img" aria-label="Illustration of green grass blades with orange, pink and yellow flowers"></div>

    <svg class="contact-band" width="754" height="419" viewBox="0 0 754 419" aria-hidden="true">
      <path d="M255 322 C 330 345, 430 350, 754 310 L754 419 L255 419 Z" fill="var(--band-green)"/>
    </svg>

    <h1 class="business-name">TIDAL VERGE</h1>
    <div class="name-rule"></div>

    <ul class="service-list">
      <li>lawn mowing</li>
      <li>garden matanace</li>
      <li>jobs around the house</li>
    </ul>

    <p class="quote-line">Call for free quote <span class="phone-number">0413562049</span></p>
    <p class="email-line">email: norma.vance@fernmail.com.au</p>
  </section>
</body>
</html>
```